Business Design for Printed Shipping Tape

We need a company logo design to be printed on packaging natural color WAT tape for shipping boxes. www.brightmeadowkelp.com
The tape is 3" wide. Repeat pattern every 10 inches.
Would like our website vertical at one end side and "The Future of Nutrition" on the opposite end.

Industry/Entity Type

Health, Nutrition

Font styles to use
Sans Serif

Requirements
Must have
• Company Logo (attached) website and text "The Future of Nutrition"
Nice to have
• Tape is Natural Color.

```html
<!DOCTYPE html>
<html lang="en">
<head>
<meta charset="utf-8">
<title>Bright Meadow Kelp – Shipping Tape</title>
<link rel="stylesheet" href="https://fonts.googleapis.com/css2?family=Montserrat:wght@400;800&display=swap">
<style>
  :root {
    --backdrop: #e4e4e4;
    --tape: #a68d6f;
    --ink: #0d0d0d;
    --band: #050505;
    --band-text: #ffffff;
    --kelp-green: #0e5a45;
  }
  html, body {
    margin: 0;
    width: 1200px;
    height: 960px;
    overflow: hidden;
    background: var(--backdrop);
    font-family: "Montserrat", sans-serif;
  }
  .tape {
    position: absolute;
    left: 0;
    top: 315px;
    width: 1200px;
    height: 330px;
    background: var(--tape);
    box-shadow: 0 6px 18px rgba(0,0,0,0.12);
  }
  .brand-mark {
    position: absolute;
    left: 60px;
    top: 110px;
    width: 110px;
    height: 110px;
    border-radius: 50%;
    background: var(--kelp-green);
  }
  .brand-name {
    position: absolute;
    left: 200px;
    top: 100px;
    margin: 0;
    font-weight: 800;
    font-size: 46px;
    line-height: 1;
    color: var(--ink);
    text-transform: uppercase;
    white-space: nowrap;
  }
  .tagline {
    position: absolute;
    left: 202px;
    top: 206px;
    font-weight: 400;
    font-size: 17px;
    letter-spacing: 2px;
    color: var(--ink);
    text-transform: uppercase;
    white-space: nowrap;
  }
  .slogan {
    position: absolute;
    left: 690px;
    top: 120px;
    width: 200px;
    font-weight: 800;
    font-size: 22px;
    line-height: 1.15;
    text-align: center;
    color: var(--ink);
    text-transform: uppercase;
    transform: rotate(180deg);
  }
  .web-band {
    position: absolute;
    left: 910px;
    top: 0;
    width: 240px;
    height: 330px;
    background: var(--band);
    display: flex;
    align-items: center;
    justify-content: center;
  }
  .web-address {
    font-weight: 800;
    font-size: 14px;
    line-height: 1.25;
    text-align: center;
    color: var(--band-text);
    text-transform: uppercase;
    transform: rotate(180deg);
    white-space: nowrap;
  }
</style>
</head>
<body>
  <div class="tape">
    <div class="brand-mark"></div>
    <h1 class="brand-name">Bright Meadow<br>Kelp</h1>
    <div class="tagline">A Daily Dose of Green</div>
    <div class="slogan">The Future of<br>Nutrition</div>
    <div class="web-band">
      <div class="web-address">www.<br>brightmeadowkelp.com</div>
    </div>
  </div>
</body>
</html>
```